Norwegian psychologist service needs a fresh and exiting web site*

Norwegian psychologist service: working with therapy, personal development, mastery and personal growth. Focus: children and teenagers with special needs; family dynamics; group processes; individuals with a need for therapy and personal growth. (Our company name: Kildeløft og ro (means Mastery and Growth).

We already have a logo for the company, which will be used (will be attached in the project).

The webside is to be structured in 4 pages with roll down curtain menus (the numbers are just for guiding the designer - the should not be added):

Page 1: Om Kildeløft og Ro (about Mastery and Growth): this is where our business is is presented/described shortly: Lorem Ipsum dolor cit...

Page 2: Tjenester (Services): this is where our 5 service areas are presented:
2.1 Utredning (Investigation, diagnosing): Lorem Ipsum dolor cit...
2.2 Rådgivning (consulting): Lorem Ipsum dolor cit...

2.3 Kurs og work shops (courses and work shops): Lorem Ipsum dolor cit...
2.3a Kildeløft og ro Tema 1 (T1)
2.3b Kildeløft og ro Tema 2 (T2)
2.3c Kildeløft og ro Tema 3 (T3)

2.4 Terapi og utvikling (Therapy and development)
2.4a Kildeløft og ro for individer (KR1)
2.4b Kildeløft og ro i familier (KR2)
2.4c Kildeløft og ro i grupper (KR3)
2.4d Kildeløft og ro i institusjoner (KR4)

Page 3: Aktuelt (Blog): this is our blog where we share knowledge and articles

Page 4: Kontakt (Contact): This is the contact form page. Contact form should constitute:
- Ditt navn (your name)
- E-post (your e-mail)
- Emne (subject)
- Melding (message/description)

Our project should also include suggestion for handheld units (iPhone, iPad).
Updates

We have both been traveling with work for a while, and then unfortunately both of us got sick on return, so we need a few more days to evaluate and choose design. Kind Regards Arne & Ragnhild

Target Market(s)

Focus on therapy, learning, mastery and growth for children and teenagers with special needs, within the family dynamics, or in a group setting.
OUR MARKETS:
Private market: individuals, families, groups and health industry institutions (with focus on learning, mastery, growth (as well as growing up) and psychiatry for children and teenagers with special difficulties and needs)
Public institutions: Government institutions, state institutions and municipality institutions (e.g. schools, municipality health service, hospitals) that serve the public (families with children and teenagers with special needs, and where learning, mastery, growth (as well as growing up) and potential psychiatry is an issue).

Number of Pages Required

4 page

Font styles to use
Sans Serif

Colors

Designer to choose colors to be used in the design.

Requirements
Must have
• The website must have 4 pages with roll down curtain menus (we have added a PDF with suggested structure, and headings, with sub menus - see attached PDF drawing.
• The web page must also use the added logo file - and make the web page work well with our logo.
• We would like the website to have a modern look and we would like the site to be associated with typical HIGH END TOP QUALITY private health institutions, but with a stronger focus on human beings (hands, faces etc), and not white coats and doctors. We are psychologists in the private market.
• For instance, if photos are being used - we tend to like "warm" almost art-like, "grainy" two-tone (e.g. sepia) photos to illustrate our focus. If designer can find such photos as part of design, it would be interesting to us. We would like a few photos like that integrated in the design.
• We also want a design suggestion for how the web page should look like and behave on handheld units (e.g. iPhone, iPad).
Nice to have
• If designer could find a number of suitable photos that matches the business idea and design requirements (see description above), that could follow website, that would be good.
• It could also be nice to have graphic symbols that denote the different pages/subpages (subjects)....
• HORSES: we sometimes use horses as a "tool" in therapy sessions. The horse is not necessarily used for riding, but for contact, communication and grooming. PHOTOS: we would like the designer to find an opportunity for using a photo reflecting this cooperation between therapist, child, teenager and horse. It is a bit up to the designer to find a way to do this... Since the horse is only a tool, among many other tools, it does not have to be much - but we want to try and see how it will work with a photo that also reflects this part of our business.

```html
<!DOCTYPE html>
<html lang="no">
<head>
<meta charset="utf-8">
<title>Kildeløft og ro</title>
<link href="https://fonts.googleapis.com/css2?family=IBM+Plex+Sans:wght@400;500;600;700&family=Poppins:wght@400;500;600&family=Lora:wght@700&display=swap" rel="stylesheet">
<style>
:root{
  --navy:#1b2160;
  --navy-panel:#252d80;
  --green:#0f5a36;
  --green-dark:#0c3a22;
  --mint:#e7f3ee;
  --hero-bg:#e3e6e8;
  --field:#6072f3;
  --ink:#222;
  --footer:#121212;
}
*{margin:0;padding:0;box-sizing:border-box}
html,body{width:1200px;height:3960px;overflow:hidden;background:#fff}
body{position:relative;font-family:"Poppins",sans-serif;color:var(--ink)}
.abs{position:absolute}
.heading{font-family:"IBM Plex Sans",sans-serif;font-weight:700}

/* header */
.logo{left:138px;top:60px;width:200px;text-align:center}
.logo-mark{display:block;width:34px;height:34px;border-radius:50%;background:var(--navy);margin:0 auto 10px}
.logo-name{font-family:"IBM Plex Sans",sans-serif;font-weight:500;font-size:27px;color:var(--navy);letter-spacing:.5px}
.social-pill{left:750px;top:0;width:292px;height:42px;background:var(--navy);border-radius:0 0 30px 30px;display:flex;align-items:center;color:#fff;font-size:14px}
.social-pill span{padding:0 18px;border-right:1px solid rgba(255,255,255,.4);height:42px;display:flex;align-items:center}
.social-pill i{width:45px;height:42px;border-right:1px solid rgba(255,255,255,.4);display:flex;align-items:center;justify-content:center}
.social-pill i::after{content:"";width:10px;height:10px;border-radius:50%;background:rgba(255,255,255,.8)}
.contact-item{top:68px;display:flex;gap:14px;align-items:center;font-size:15px;line-height:1.25;color:#333}
.contact-item b{font-weight:600;font-size:13px}
.navbar{left:0;top:135px;width:1200px;height:62px}
.nav{left:386px;top:157px;display:flex;font-size:13px;color:#fff;text-transform:uppercase}
.nav li{list-style:none;margin-right:22px}
.nav li+li::before{content:"•";margin-right:22px}
.btn-quote{left:903px;top:144px;width:140px;height:43px;background:var(--green);color:#fff;font-family:"IBM Plex Sans",sans-serif;font-weight:700;font-size:14px;display:flex;align-items:center;justify-content:center}

/* hero */
.hero-bg{left:0;top:197px;width:1200px;height:700px;background:linear-gradient(90deg,#dfe3e6,#e4e7e9 60%,#e1e5e7)}
.hero-photo{left:0;top:197px;width:680px;height:700px;
  background:
    radial-gradient(ellipse 120px 150px at 240px 200px,#f3d4c2 0%,rgba(243,212,194,0) 100%),
    radial-gradient(ellipse 170px 200px at 430px 560px,#d9b38f 0%,rgba(217,179,143,0) 100%),
    radial-gradient(ellipse 230px 260px at 200px 520px,#efc3b3 0%,rgba(239,195,179,0) 100%),
    radial-gradient(ellipse 160px 240px at 420px 150px,#b9c8c9 0%,rgba(185,200,201,0) 100%),
    linear-gradient(160deg,#e6e8ea 0%,#ebd6cb 45%,#d8b7a3 80%,#c9ab94 100%);
  -webkit-mask-image:linear-gradient(90deg,#000 78%,transparent 100%);
  mask-image:linear-gradient(90deg,#000 78%,transparent 100%)}
.mint{left:0;top:880px;width:1200px;height:526px;background:var(--mint)}
.hero-title{left:610px;top:402px;font-size:63px;line-height:68px;color:var(--navy);letter-spacing:1px}
.hero-text{left:615px;top:555px;width:530px;font-size:12px;line-height:20px;color:#222}
.btn{display:flex;align-items:center;justify-content:center;gap:18px;background:var(--green);color:#fff;font-family:"Lora",serif;font-weight:700;font-size:12px;letter-spacing:.5px}
.arrow{width:24px;height:10px}

/* about */
.about-title{left:143px;top:990px;font-size:48px;color:var(--ink)}
.about-sub{left:143px;top:1042px;font-size:25px;font-weight:600;color:var(--ink);font-family:"IBM Plex Sans",sans-serif}
.about-text{left:143px;top:1090px;width:424px;font-size:11.6px;line-height:18px;text-align:justify;color:#333}
.frame-outer{left:645px;top:971px;width:424px;height:350px;border:1px solid #d5dfdb}
.frame-line{left:612px;top:1006px;width:20px;height:277px;border:2px solid var(--navy);border-right:none}
.about-photo{left:630px;top:993px;width:413px;height:305px;
  background:
    radial-gradient(ellipse 70px 90px at 300px 80px,#f0cdb8 0%,rgba(240,205,184,0) 100%),
    radial-gradient(ellipse 90px 120px at 320px 230px,#eaeff6 0%,rgba(234,239,246,0) 100%),
    radial-gradient(ellipse 80px 110px at 90px 170px,#d6c2a6 0%,rgba(214,194,166,0) 100%),
    radial-gradient(ellipse 60px 60px at 160px 35px,#d85a4a 0%,rgba(216,90,74,0) 100%),
    radial-gradient(ellipse 50px 70px at 165px 170px,#3f66b8 0%,rgba(63,102,184,0) 100%),
    radial-gradient(ellipse 50px 50px at 385px 60px,#e6b930 0%,rgba(230,185,48,0) 100%),
    linear-gradient(120deg,#ebe7df 0%,#d4dae3 45%,#dcd6cb 70%,#cfd6e0 100%)}

/* services */
.section-title{font-size:47px;color:var(--green-dark);letter-spacing:1px}
.phone{width:167px;height:362px;border:5px solid #1c1c1c;border-radius:18px;background:#fff;overflow:hidden}
.phone-icon{position:absolute;left:0;top:22px;width:100%;height:100px;display:flex;align-items:center;justify-content:center}
.phone-photo{position:absolute;left:0;bottom:0;width:100%;height:212px}
.panel{width:262px;height:209px;background:var(--navy-panel);color:#fff;padding:34px 18px 0 21px}
.panel h3{font-family:"IBM Plex Sans",sans-serif;font-weight:600;font-size:15px;margin-bottom:14px;letter-spacing:.3px;white-space:nowrap}
.panel p{font-size:11px;line-height:18px}
.panel .mini{margin-top:18px;width:88px;height:26px;background:#fff;color:var(--green);font-family:"Lora",serif;font-size:8px;display:flex;align-items:center;justify-content:center;gap:10px}

/* articles */
.article{background:
    radial-gradient(ellipse 90px 70px at 75% 30%,rgba(200,214,206,.55) 0%,rgba(200,214,206,0) 100%),
    radial-gradient(ellipse 80px 120px at 20% 25%,rgba(40,60,60,.35) 0%,rgba(40,60,60,0) 100%),
    linear-gradient(150deg,#7fa094,#5d8677 60%,#6f978a);color:#fff;padding:0 34px}
.article h4{font-weight:500;font-size:14.5px;line-height:25px}
.article .meta{display:flex;gap:36px;font-size:11px;font-weight:600;margin-top:20px;font-family:"IBM Plex Sans",sans-serif}
.meta span{display:flex;align-items:center;gap:8px}
.meta span::before{content:"";width:11px;height:11px;border:1.5px solid #fff;border-radius:50%}

/* contact */
.contact-bg{left:0;top:3174px;width:1200px;height:480px;background:
    radial-gradient(ellipse 120px 200px at 120px 420px,rgba(150,150,150,.35) 0%,rgba(150,150,150,0) 100%),
    radial-gradient(ellipse 160px 220px at 1050px 400px,rgba(140,140,140,.35) 0%,rgba(140,140,140,0) 100%),
    linear-gradient(180deg,#f3f3f3,#e1e1e1)}
.field{background:var(--field);color:#fff;font-size:10px;padding:14px 14px;text-transform:uppercase}
.btn-send{left:143px;top:3558px;width:200px;height:40px;border:1.5px solid var(--green);color:var(--green);font-family:"Lora",serif;font-weight:700;font-size:11.5px;display:flex;align-items:center;justify-content:center;gap:24px;letter-spacing:.5px}
.info{left:713px;font-size:17px;color:#333;display:flex;align-items:center;gap:14px}
.round{width:32px;height:32px;border-radius:50%}

/* footer */
.footer{left:0;top:3654px;width:1200px;height:306px;background:var(--footer)}
.footer-logo{left:500px;top:3715px;width:200px;text-align:center}
.footer-logo .logo-mark{background:#fff}
.footer-logo .logo-name{color:#fff}
.footer-nav{top:3848px;left:0;width:1200px;display:flex;justify-content:center;gap:48px;color:#fff;font-size:12.5px;list-style:none}
.copyright{top:3896px;left:0;width:1200px;text-align:center;color:#fff;font-size:11.5px}
</style>
</head>
<body>

<!-- header -->
<div class="abs logo"><span class="logo-mark"></span><span class="logo-name">Kildeløft og ro</span></div>
<div class="abs social-pill"><span>FØLG OSS PÅ</span><i></i><i></i></div>
<div class="abs contact-item" style="left:435px">
  <svg width="42" height="32" viewBox="0 0 42 32"><rect x="1" y="1" width="40" height="30" rx="2" fill="var(--green)"/><path d="M2 3 L21 18 L40 3" stroke="#fff" stroke-width="3" fill="none"/></svg>
  <div><b>E-POST:</b><br>01-470 5518</div>
</div>
<div class="abs contact-item" style="left:622px">
  <svg width="32" height="32" viewBox="0 0 24 24"><path d="M6.6 10.8c1.4 2.8 3.8 5.1 6.6 6.6l2.2-2.2c.3-.3.7-.4 1-.2 1.1.4 2.3.6 3.6.6.6 0 1 .4 1 1V20c0 .6-.4 1-1 1C10.6 21 3 13.4 3 4c0-.6.4-1 1-1h3.5c.6 0 1 .4 1 1 0 1.3.2 2.5.6 3.6.1.3 0 .7-.2 1z" fill="var(--green)"/></svg>
  <div><b>ANROP:</b><br>555-210-3846</div>
</div>
<svg class="abs navbar" viewBox="0 0 1200 62" preserveAspectRatio="none"><polygon points="362,0 1200,0 1200,62 0,62 0,31 332,31" fill="var(--navy)"/></svg>
<ul class="abs nav"><li>Hjem</li><li>Om oss</li><li>Tjenester</li><li>Blogg</li><li>Kontakt oss</li></ul>
<div class="abs btn-quote">GET A QUOTE</div>

<!-- hero -->
<div class="abs hero-bg"></div>
<div class="abs hero-photo" role="img" aria-label="Smilende kvinne med briller sammen med et barn med flettet hår"></div>
<svg class="abs" style="left:0;top:840px" width="1200" height="60" viewBox="0 0 1200 60" preserveAspectRatio="none"><path d="M0 30 C200 -10 420 60 640 38 C860 16 1000 10 1200 40 L1200 60 L0 60 Z" fill="var(--mint)"/></svg>
<div class="abs mint"></div>
<h1 class="abs heading hero-title">LOREM IPSUM<br>DOLOR SIT AMET</h1>
<p class="abs hero-text">Lorem ipsum dolor sit amet, consectetur adipiscing elit, sed do eiusmod tempor incididunt ut labore et dolore magna aliqua.</p>
<div class="abs btn" style="left:619px;top:630px;width:132px;height:41px">LES MER <svg class="arrow" viewBox="0 0 24 10"><path d="M0 5H22M17 1L22 5L17 9" stroke="#fff" stroke-width="1.5" fill="none"/></svg></div>

<!-- about -->
<h2 class="abs heading about-title">OM</h2>
<div class="abs about-sub">KILDELØFT OG RO</div>
<p class="abs about-text">Lorem ipsum dolor sit amet, consectetur adipiscing elit, sed do eiusmod tempor incididunt ut labore et dolore magna aliqua. Ut enim ad minim veniam, quis nostrud exercitation ullamco laboris nisi ut aliquip ex ea commodo consequat. Duis aute irure dolor in reprehenderit in voluptate velit esse cillum dolore eu fugiat nulla pariatur. Excepteur sint occaecat cupidatat non proident, sunt in culpa qui officia deserunt mollit anim id est laborum.</p>
<div class="abs btn" style="left:146px;top:1238px;width:132px;height:40px">LES MER <svg class="arrow" viewBox="0 0 24 10"><path d="M0 5H22M17 1L22 5L17 9" stroke="#fff" stroke-width="1.5" fill="none"/></svg></div>
<div class="abs frame-outer"></div>
<div class="abs frame-line"></div>
<div class="abs about-photo" role="img" aria-label="Terapeut som viser et kort til en jente ved en hylle med fargerike leker"></div>

<!-- services -->
<h2 class="abs heading section-title" style="left:142px;top:1512px">VÅRE TJENESTER</h2>

<div class="abs phone" style="left:143px;top:1609px">
  <div class="phone-icon"><svg width="72" height="72" viewBox="0 0 72 72"><circle cx="30" cy="30" r="22" stroke="var(--navy)" stroke-width="6" fill="none"/><path d="M46 46L64 64" stroke="var(--navy)" stroke-width="8" stroke-linecap="round"/><path d="M20 36a12 8 0 0 0 20 0" stroke="var(--navy)" stroke-width="4" fill="none"/></svg></div>
  <div class="phone-photo" role="img" aria-label="Kvinne med kaffekopp i samtale" style="background:radial-gradient(ellipse 50px 70px at 110px 50px,#e8c7b0 0%,rgba(232,199,176,0) 100%),radial-gradient(ellipse 60px 90px at 100px 150px,#d9cbb6 0%,rgba(217,203,182,0) 100%),radial-gradient(ellipse 30px 60px at 20px 100px,#f4f4f2 0%,rgba(244,244,242,0) 100%),linear-gradient(160deg,#e6e1da,#c7b8a6 60%,#b9b4ad)"></div>
</div>
<div class="abs panel" style="left:310px;top:1762px"><h3>ETTERFORSKNING</h3><p>Lorem ipsum dolor sit amet, consectetur adipiscing elit, sed do eiusmod tempor incididunt ut labore et dolore magna</p><div class="mini">LES MER <svg width="14" height="8" viewBox="0 0 24 10"><path d="M0 5H22M17 1L22 5L17 9" stroke="var(--green)" stroke-width="2" fill="none"/></svg></div></div>

<div class="abs phone" style="left:616px;top:1609px">
  <div class="phone-icon"><svg width="80" height="64" viewBox="0 0 80 64"><circle cx="40" cy="14" r="10" fill="var(--navy)"/><circle cx="16" cy="24" r="8" fill="var(--navy)"/><circle cx="64" cy="24" r="8" fill="var(--navy)"/><path d="M26 62V42a14 14 0 0 1 28 0v20z" fill="var(--navy)"/><path d="M4 62V46a12 12 0 0 1 20 -6v22z M76 62V46a12 12 0 0 0 -20 -6v22z" fill="var(--navy)"/></svg></div>
  <div class="phone-photo" role="img" aria-label="Kvinne som skriver notater ved et bord" style="background:radial-gradient(ellipse 40px 60px at 75px 60px,#d8b39c 0%,rgba(216,179,156,0) 100%),radial-gradient(ellipse 80px 40px at 80px 190px,#efe9e1 0%,rgba(239,233,225,0) 100%),radial-gradient(ellipse 60px 110px at 70px 90px,#2e2b2a 0%,rgba(46,43,42,0) 100%),linear-gradient(160deg,#6a625c,#9a8f86 55%,#d8d2ca)"></div>
</div>
<div class="abs panel" style="left:783px;top:1762px"><h3>RÅDGIVNING</h3><p>Lorem ipsum dolor sit amet, consectetur adipiscing elit, sed do eiusmod tempor incididunt ut labore et dolore magna</p><div class="mini">LES MER <svg width="14" height="8" viewBox="0 0 24 10"><path d="M0 5H22M17 1L22 5L17 9" stroke="var(--green)" stroke-width="2" fill="none"/></svg></div></div>

<div class="abs phone" style="left:143px;top:2014px">
  <div class="phone-icon"><svg width="72" height="72" viewBox="0 0 72 72"><g fill="var(--navy)"><path d="M6 50L40 36L66 48L32 64Z"/><path d="M6 36L40 22L66 34L32 50Z"/><path d="M6 22L40 8L66 20L32 36Z"/></g><path d="M10 52L32 60M10 38L32 46M10 24L32 32" stroke="#fff" stroke-width="2"/></svg></div>
  <div class="phone-photo" role="img" aria-label="Smilende mann i dress" style="background:radial-gradient(ellipse 40px 55px at 70px 60px,#d9ab8c 0%,rgba(217,171,140,0) 100%),radial-gradient(ellipse 70px 80px at 75px 180px,#3a4152 0%,rgba(58,65,82,0) 100%),radial-gradient(ellipse 40px 90px at 140px 90px,#e9edf1 0%,rgba(233,237,241,0) 100%),linear-gradient(160deg,#cfd6dc,#9a948e 50%,#4d5262)"></div>
</div>
<div class="abs panel" style="left:310px;top:2168px"><h3>KURS OG ARBEIDSBUTIKKER</h3><p>Lorem ipsum dolor sit amet, consectetur adipiscing elit, sed do eiusmod tempor incididunt ut labore et dolore magna</p><div class="mini">LES MER <svg width="14" height="8" viewBox="0 0 24 10"><path d="M0 5H22M17 1L22 5L17 9" stroke="var(--green)" stroke-width="2" fill="none"/></svg></div></div>

<div class="abs phone" style="left:616px;top:2014px">
  <div class="phone-icon"><svg width="76" height="76" viewBox="0 0 76 76"><circle cx="38" cy="38" r="28" stroke="var(--navy)" stroke-width="10" stroke-dasharray="9 5" fill="none"/><circle cx="38" cy="38" r="20" fill="#fff" stroke="var(--navy)" stroke-width="4"/><path d="M31 34a7 7 0 1 1 14 0c0 4-4 5-4 9h-6c0-4-4-5-4-9z" fill="var(--navy)"/><rect x="34" y="45" width="8" height="4" fill="var(--navy)"/></svg></div>
  <div class="phone-photo" role="img" aria-label="Hender som arbeider med lapper og papirer på et bord" style="background:radial-gradient(ellipse 60px 40px at 60px 110px,#efe7d6 0%,rgba(239,231,214,0) 100%),radial-gradient(ellipse 20px 15px at 40px 90px,#e8d66a 0%,rgba(232,214,106,0) 100%),radial-gradient(ellipse 20px 15px at 100px 130px,#e89aa8 0%,rgba(232,154,168,0) 100%),radial-gradient(ellipse 40px 50px at 120px 70px,#d2a88b 0%,rgba(210,168,139,0) 100%),linear-gradient(160deg,#7f97aa,#c9c2b4 55%,#a9a39a)"></div>
</div>
<div class="abs panel" style="left:783px;top:2168px"><h3>TERAPI OG UTVIKLING</h3><p>Lorem ipsum dolor sit amet, consectetur adipiscing elit, sed do eiusmod tempor incididunt ut labore et dolore magna</p><div class="mini">LES MER <svg width="14" height="8" viewBox="0 0 24 10"><path d="M0 5H22M17 1L22 5L17 9" stroke="var(--green)" stroke-width="2" fill="none"/></svg></div></div>

<!-- articles -->
<h2 class="abs heading section-title" style="left:142px;top:2502px">NYE ARTIKLER</h2>

<article class="abs article" role="img" aria-label="Forretningsfolk ved et bord med nettbrett" style="left:143px;top:2603px;width:284px;height:170px;padding-top:56px"><h4>Lorem ipsum dolor sit amet,<br>consectetur adipiscing elit,</h4><div class="meta"><span>FEB 12, 2020</span><span>ADMIN</span></div></article>
<article class="abs article" role="img" aria-label="Forretningsfolk ved et bord med nettbrett" style="left:143px;top:2796px;width:284px;height:169px;padding-top:56px"><h4>Lorem ipsum dolor sit amet,<br>consectetur adipiscing elit,</h4><div class="meta"><span>FEB 12, 2020</span><span>ADMIN</span></div></article>
<article class="abs article" role="img" aria-label="Person i dress som holder et nettbrett" style="left:453px;top:2601px;width:284px;height:364px;padding-top:248px"><h4>Lorem ipsum dolor sit amet,<br>consectetur adipiscing elit,</h4><div class="meta"><span>FEB 12, 2020</span><span>ADMIN</span></div></article>
<article class="abs article" role="img" aria-label="Person i dress som holder et nettbrett" style="left:759px;top:2601px;width:284px;height:364px;padding-top:248px"><h4>Lorem ipsum dolor sit amet,<br>consectetur adipiscing elit,</h4><div class="meta"><span>FEB 12, 2020</span><span>ADMIN</span></div></article>

<div class="abs btn" style="left:501px;top:3002px;width:200px;height:42px">SE ALLE ARTIKLER <svg class="arrow" viewBox="0 0 24 10"><path d="M0 5H22M17 1L22 5L17 9" stroke="#fff" stroke-width="1.5" fill="none"/></svg></div>

<!-- contact -->
<div class="abs contact-bg" role="img" aria-label="Dempet silhuett av mennesker i et lyst kontorlokale"></div>
<h2 class="abs heading section-title" style="left:143px;top:3228px">TA KONTAKT</h2>
<div class="abs field" style="left:143px;top:3311px;width:260px;height:40px">Ditt navn</div>
<div class="abs field" style="left:423px;top:3311px;width:259px;height:40px">E-post</div>
<div class="abs field" style="left:143px;top:3368px;width:539px;height:40px">Emne</div>
<div class="abs field" style="left:143px;top:3423px;width:539px;height:103px">Melding</div>
<div class="abs btn-send">SENDE MELDING <svg width="18" height="16" viewBox="0 0 24 22"><path d="M1 10L23 1L17 21L11 13Z" fill="var(--green)"/></svg></div>

<h2 class="abs heading section-title" style="left:713px;top:3228px">KONTAKTINFO</h2>
<div class="abs info" style="top:3308px"><svg width="18" height="22" viewBox="0 0 18 24"><path d="M9 1a8 8 0 0 0-8 8c0 6 8 14 8 14s8-8 8-14a8 8 0 0 0-8-8z" fill="none" stroke="var(--green)" stroke-width="2.5"/><circle cx="9" cy="9" r="3" fill="var(--green)"/></svg>Fjordveien 14</div>
<div class="abs info" style="top:3360px"><svg width="22" height="22" viewBox="0 0 24 24"><path d="M6.6 10.8c1.4 2.8 3.8 5.1 6.6 6.6l2.2-2.2c.3-.3.7-.4 1-.2 1.1.4 2.3.6 3.6.6.6 0 1 .4 1 1V20c0 .6-.4 1-1 1C10.6 21 3 13.4 3 4c0-.6.4-1 1-1h3.5c.6 0 1 .4 1 1 0 1.3.2 2.5.6 3.6.1.3 0 .7-.2 1z" fill="var(--green)"/></svg>555-210-384</div>
<div class="abs info" style="top:3428px"><svg width="22" height="20" viewBox="0 0 24 22"><path d="M1 10L23 1L17 21L11 13Z" fill="var(--green)"/></svg>post@kildeloft-eksempel.no</div>
<div class="abs round" style="left:716px;top:3495px;background:#777"></div>
<div class="abs round" style="left:758px;top:3495px;background:var(--green)"></div>

<!-- footer -->
<footer class="abs footer"></footer>
<div class="abs footer-logo"><span class="logo-mark"></span><span class="logo-name">Kildeløft og ro</span></div>
<ul class="abs footer-nav"><li>HJEM</li><li>OM OSS</li><li>TJENESTER</li><li>BLOGG</li><li>KONTAKT OSS</li></ul>
<p class="abs copyright">Copyright © 2020. All Right Reserved.</p>

</body>
</html>
```